Tennly Packaging Business Card

Project Overview
We are seeking a modern, minimalist business card that effectively represents our company while making a bold and lasting impression. The design should reflect trust, professionalism, and innovation, reinforcing our expertise in custom plastic manufacturing for warehouse and distribution centers.

Provided Assets & Specifications
Logo: We will provide our official logo for integration into the design.
Design Files: Photoshop (PSD) files for our printing specifications will be supplied.

Card Size & Material:
Dimensions: 3.5" x 2"
Material: 1/8" Radius Plastic Business Cards with 1/8" Rounded Corners
Clear plastic background—the design should strategically incorporate transparency.
Orientation: The card should be designed in landscape format for a sleek and professional presentation.

Design Requirements:
Logo Prominence
The logo must be the focal point of the card.
Space should be used effectively to draw attention to the logo while maintaining a minimalist layout.

Clear Plastic Integration
The transparent background should create the illusion of blank space, enhancing the modern and high-quality feel.
Avoid any frosted effects—we do not want white areas to appear semi-transparent.

Minimalist & Impactful
Clean, structured, and easy to read at a glance.
Focus on sharp contrast to ensure legibility and visibility.
The design should instill confidence and reflect our role as a leading plastics manufacturer.

Color Palette & Contrast
Primary Colors: Blue, Black, White, and Grey
Use bold black or blue for text and key elements to ensure they stand out against the clear plastic.
Avoid light, pastel, or neon colors that may fade into the plastic background.
No frosted or semi-transparent white—we do not want a cloudy effect.

Typography & Information Hierarchy
Bold, modern typography—clear, professional, and highly legible.
The business card should highlight:
Company Logo (Primary Focus)
Full Name & Title
Phone Number
Email
Website

Brand Representation
The card should reflect our expertise in manufacturing high-quality custom plastics for large-scale packaging and distribution businesses.
Our clients rely on us to enhance their brand presence through custom plastic solutions, and our business cards should reinforce that sense of precision and trust.

Final Considerations
Utilize the clear plastic effectively to differentiate our brand from standard business cards.
Maintain a sleek, professional aesthetic while ensuring all text and elements remain legible.
The design should align with our industry, conveying reliability and innovation.
We look forward to seeing a design that captures our brand identity, maximizes the clear plastic medium, and makes a strong, professional impact on our clients.

```html
<!DOCTYPE html>
<html lang="en">
<head>
<meta charset="UTF-8">
<title>Tennly Packaging Business Card</title>
<link href="https://fonts.googleapis.com/css2?family=Lato:wght@400;700&display=swap" rel="stylesheet">
<style>
  :root {
    --page-bg: #d8d5d1;
    --card-clear: #eceeef;
    --card-edge: #c9cdd0;
    --ink-dark: #333333;
    --ink-mid: #4a4a4a;
    --brand-blue: #1f6e8c;
    --band-black: #1b1b1b;
    --web-gold: #c9bd9f;
  }
  * { margin: 0; padding: 0; box-sizing: border-box; }
  html, body {
    width: 1200px;
    height: 968px;
    overflow: hidden;
    background: var(--page-bg);
    font-family: "Lato", Arial, sans-serif;
  }
  .business-card {
    position: absolute;
    left: 172px;
    top: 270px;
    width: 857px;
    height: 474px;
    background: var(--card-clear);
    border: 1px solid var(--card-edge);
    border-radius: 20px;
    overflow: hidden;
    box-shadow: 0 10px 30px rgba(0,0,0,0.12);
  }
  .brand-lockup {
    position: absolute;
    right: 50px;
    top: 98px;
    display: flex;
    align-items: center;
    gap: 14px;
    height: 46px;
  }
  .brand-square {
    width: 38px;
    height: 38px;
    background: var(--brand-blue);
  }
  .brand-name {
    font-weight: 700;
    font-size: 40px;
    line-height: 46px;
    color: var(--brand-blue);
  }
  .holder-name {
    position: absolute;
    left: 43px;
    top: 246px;
    font-weight: 700;
    font-size: 35px;
    line-height: 44px;
    color: var(--ink-dark);
  }
  .holder-title {
    position: absolute;
    left: 43px;
    top: 293px;
    font-size: 20px;
    line-height: 26px;
    color: var(--ink-mid);
  }
  .divider {
    position: absolute;
    left: 43px;
    right: 50px;
    top: 337px;
    height: 2px;
    background: var(--ink-dark);
  }
  .contact-list {
    position: absolute;
    left: 43px;
    top: 353px;
    list-style: none;
  }
  .contact-list li {
    display: flex;
    align-items: center;
    gap: 20px;
    height: 36px;
    font-size: 21px;
    color: var(--ink-dark);
  }
  .contact-list svg { width: 24px; height: 24px; fill: var(--brand-blue); flex: none; }
  .address {
    position: absolute;
    right: 50px;
    top: 361px;
    text-align: right;
    font-size: 21px;
    line-height: 30px;
    color: var(--band-black);
  }
  .bottom-bands {
    position: absolute;
    left: 0;
    bottom: 0;
    width: 857px;
    height: 34px;
  }
  .website {
    position: absolute;
    right: 50px;
    bottom: 4px;
    font-size: 20px;
    line-height: 26px;
    color: var(--web-gold);
    letter-spacing: 0.5px;
  }
</style>
</head>
<body>
  <div class="business-card">
    <div class="brand-lockup">
      <div class="brand-square"></div>
      <div class="brand-name">Tennly Packaging</div>
    </div>

    <div class="holder-name">MARCUS HALE</div>
    <div class="holder-title">Owner</div>
    <div class="divider"></div>

    <ul class="contact-list">
      <li>
        <svg viewBox="0 0 24 24" aria-hidden="true"><path d="M6.6 10.8a15.1 15.1 0 0 0 6.6 6.6l2.2-2.2a1 1 0 0 1 1-.25 11.4 11.4 0 0 0 3.6.57 1 1 0 0 1 1 1V20a1 1 0 0 1-1 1A17 17 0 0 1 3 4a1 1 0 0 1 1-1h3.5a1 1 0 0 1 1 1c0 1.25.2 2.45.57 3.57a1 1 0 0 1-.25 1z"/></svg>
        071-380 662 915
      </li>
      <li>
        <svg viewBox="0 0 24 24" aria-hidden="true"><path d="M2 5h20v14H2z"/><path d="M2 6l10 7 10-7" fill="none" stroke="var(--card-clear)" stroke-width="1.6"/></svg>
        info@tennlypack.com
      </li>
    </ul>

    <div class="address">18, Harbor Lane Unit 7<br>Springfield 60214, Ohio</div>

    <svg class="bottom-bands" viewBox="0 0 857 34" preserveAspectRatio="none" aria-hidden="true">
      <polygon points="0,10 488,10 480,22 0,22" fill="var(--brand-blue)"/>
      <polygon points="0,26 857,26 857,34 0,34" fill="var(--band-black)"/>
      <polygon points="518,0 857,0 857,34 490,34" fill="var(--band-black)"/>
    </svg>
    <div class="website">www.tennlypack.com</div>
  </div>
</body>
</html>
```